Marwick Brewing Co Menu Design

I have an exisiting restaurant called Marwick Brewing Co. We have an official logo and an existing menu. We need something more professional and vibrant. We are a great little brewpub and need our menu to reflect the same.
Updates

I have added our existing menu that has our logo on first page. Please use and insert menu items and pricing. Thank you for all your help! I really need a great look... also our web site is marwickbrewingco.comĀ  that may help as well

I have been trying to uplaod pictures for the menu design today but for some reason I can not get them to upload on this site. Will keep trying and hope to have some posted soon.

I have submitted pictures to sketch harbor web administration and they will be posting to my project shortly.

All pictures have been posted for menu design. Thanks!

Industry/Entity Type

Restaurant

Requirements
Must have
• Great layout with pictures!!! Need it to be eye catching with current menu items and pricing. Needs to be a funtional format so I can easily changed to add or delete items as needed. I am looking for a one page menu that is 8 1/2 x 14 with front and back side print that will be placed in a clear menu cover.

```html
<!DOCTYPE html>
<html lang="en">
<head>
<meta charset="utf-8">
<title>Marwick Brewing Co – Kids Menu</title>
<link rel="stylesheet" href="https://fonts.googleapis.com/css2?family=Righteous&display=swap">
<style>
  :root {
    --paper: #fffcc4;
    --rule: #1a1a1a;
    --title-grey: #c4c4c4;
    --ring: #fff7a6;
    --plate: #dedede;
    --spoke: #2b1c6b;
    --red: #e2231a;
    --green: #0c9546;
    --slate: #4a4a58;
    --pink: #e0187c;
    --blue: #1d8fd3;
    --ink: #111111;
    --heading-red: #e8141b;
    --badge: #b9c3b2;
    --badge-ink: #7c8877;
    --contact: #3a3a3a;
  }
  html, body {
    margin: 0;
    padding: 0;
    overflow: hidden;
  }
  body {
    width: 900px;
    height: 1200px;
    position: relative;
    background: var(--paper);
    font-family: Arial, Helvetica, sans-serif;
  }
  .frame-line {
    position: absolute;
    background: var(--rule);
  }
  .frame-line.left  { left: 19px;  top: 0; width: 3px; height: 1200px; }
  .frame-line.right { left: 878px; top: 0; width: 3px; height: 1200px; }
  .frame-line.top    { left: 0; top: 14px;   width: 900px; height: 3px; }
  .frame-line.bottom { left: 0; top: 1184px; width: 900px; height: 3px; }

  .menu-title {
    position: absolute;
    right: 50px;
    top: 44px;
    margin: 0;
    font-family: "Righteous", sans-serif;
    font-size: 60px;
    letter-spacing: 3px;
    color: var(--title-grey);
    font-weight: 400;
    line-height: 1;
  }
  .menu-note {
    position: absolute;
    right: 52px;
    top: 108px;
    margin: 0;
    font-family: "Righteous", sans-serif;
    font-size: 21px;
    letter-spacing: 1px;
    color: var(--ink);
  }
  .plate-chart {
    position: absolute;
    left: 0;
    top: 0;
    width: 900px;
    height: 760px;
  }
  .plate-chart text {
    font-family: "Righteous", sans-serif;
    letter-spacing: 1px;
  }
  .section-heading {
    position: absolute;
    margin: 0;
    font-size: 17px;
    font-weight: 700;
    color: var(--heading-red);
  }
  .price-list {
    position: absolute;
    left: 35px;
    width: 820px;
    margin: 0;
    padding: 0;
    list-style: none;
    font-size: 15px;
    font-weight: 700;
    color: var(--ink);
  }
  .price-list li {
    position: relative;
    height: 20px;
    line-height: 20px;
  }
  .price-list .label { display: inline-block; width: 165px; }
  .price-list .price { position: absolute; right: 0; top: 0; }
  .dessert-line {
    position: absolute;
    left: 37px;
    top: 926px;
    width: 818px;
    margin: 0;
    font-size: 15px;
    font-weight: 700;
    color: var(--ink);
  }
  .dessert-line .price { position: absolute; right: 0; top: 0; }

  .brand-mark {
    position: absolute;
    left: 345px;
    top: 985px;
    width: 220px;
    height: 185px;
  }
  .brand-mark .disc {
    position: absolute;
    left: 35px;
    top: 0;
    width: 150px;
    height: 150px;
    border-radius: 50%;
    background: var(--badge);
  }
  .brand-mark .brand-name {
    position: absolute;
    left: 0;
    top: 155px;
    width: 220px;
    text-align: center;
    font-family: "Righteous", sans-serif;
    font-size: 20px;
    color: var(--badge-ink);
  }
  .contact {
    position: absolute;
    left: 622px;
    top: 1136px;
    margin: 0;
    font-size: 12px;
    font-weight: 700;
    color: var(--contact);
    line-height: 15px;
  }
</style>
</head>
<body>
  <div class="frame-line left"></div>
  <div class="frame-line right"></div>
  <div class="frame-line top"></div>
  <div class="frame-line bottom"></div>

  <h1 class="menu-title">KIDS 12 AND UNDER</h1>
  <p class="menu-note">*INCLUDES DRINK $6.75</p>

  <svg class="plate-chart" viewBox="0 0 900 760" aria-label="Kids meal choices">
    <ellipse cx="440" cy="455" rx="316" ry="256" fill="var(--ring)"/>
    <ellipse cx="440" cy="455" rx="265" ry="214" fill="var(--plate)"/>
    <g stroke="var(--spoke)" stroke-width="10" stroke-linecap="butt">
      <line x1="436" y1="163" x2="436" y2="455"/>
      <line x1="122" y1="455" x2="758" y2="455"/>
      <line x1="440" y1="455" x2="254" y2="606"/>
      <line x1="440" y1="455" x2="632" y2="606"/>
    </g>
    <text x="78" y="178" font-size="21" fill="var(--red)" transform="rotate(39 78 178)">GRILLED CHICKEN SANDWICH &amp; FRIES</text>
    <text x="492" y="425" font-size="21" fill="var(--green)" transform="rotate(-33 492 425)">GRILLED CHEESE ON SOURDOUGH &amp; FRIES</text>
    <text x="158" y="562" font-size="26" fill="var(--slate)" transform="rotate(-20 158 562)">CHEESE PIZZA</text>
    <text x="535" y="488" font-size="26" fill="var(--pink)" transform="rotate(20 535 488)">JR CHEESE BURGER</text>
    <text x="268" y="638" font-size="19" fill="var(--blue)">SMOKE HOUSE MAC &amp; CHEESE</text>
  </svg>

  <h2 class="section-heading" style="left:35px; top:758px;">BEVERAGES</h2>
  <ul class="price-list" style="top:778px;">
    <li>Cola, Diet Cola, Lemon-Lime, Spiced Pepper Soda, Old Mill Rootbeer, Lemonade and Strawberry Lemonade<span class="price">$2.25</span></li>
    <li><span class="label">Iced Tea</span>: Regular, Peach, Raspberry<span class="price">$2.25</span></li>
    <li><span class="label">Juice</span>: Apple, Crangrape<span class="price">$1.75</span></li>
    <li>Milk / Chocolate Milk<span class="price">$1.75</span></li>
  </ul>

  <h2 class="section-heading" style="left:38px; top:905px;">DESSERT</h2>
  <p class="dessert-line">CHOCOLATE LAVA CAKE: Served with whip cream, powder sugar and chocolate sauce drizzle<span class="price">$4.95</span></p>

  <div class="brand-mark">
    <div class="disc"></div>
    <div class="brand-name">Marwick Brewing Co</div>
  </div>

  <p class="contact">Phone: 909-555-0172<br>Email:marwickbrewing@harbormail.net</p>
</body>
</html>
```